Advertisement Design Project

I need a half page advert to be designed to appear in a magazine titled The Prudent Nest Ledger that focuses on finance and self-managed superannuation in Australia.
My client has provided a mock advert with the content that they would like jazzed up to a more professional feel.
Below is a link to view a previous copy of the magazine the advert will be appearing in.
http://www.brackenpress.com.au/PNLmagazine/pnlwin12-13/index.html
Please dont hesitate to contact me if you have any questions.
Thanks
Doug Ferrow
Target Market(s)
Investors, aged 40-70
Industry/Entity Type
Finance
Look and feel

```html
<!DOCTYPE html>
<html lang="en">
<head>
<meta charset="utf-8">
<title>Tax Free Property Investment Advert</title>
<link href="https://fonts.googleapis.com/css2?family=Archivo+Black&family=Montserrat:wght@500;600;700&display=swap" rel="stylesheet">
<style>
  :root {
    --bg: #1b1a1a;
    --deep-red: #7a1010;
    --red: #d42121;
    --bright-red: #e02a2a;
    --soft-red: #c93434;
    --white: #f4f4f4;
  }
  * { margin: 0; padding: 0; box-sizing: border-box; }
  html, body { width: 1200px; height: 880px; overflow: hidden; background: var(--bg); }
  .advert {
    position: relative; width: 1200px; height: 880px;
    background: var(--bg); color: var(--white);
    font-family: "Montserrat", Arial, sans-serif;
  }
  .kicker {
    position: absolute; top: 28px; left: 0; width: 100%;
    text-align: center; font-family: "Archivo Black", Arial, sans-serif;
    font-size: 31px; letter-spacing: 1px; color: var(--deep-red);
  }
  .rule {
    position: absolute; top: 72px; left: 88px; width: 1024px; height: 4px;
    background: var(--deep-red);
  }
  .headline {
    position: absolute; top: 76px; left: 0; width: 100%;
    text-align: center; font-family: "Archivo Black", Arial, sans-serif;
    font-size: 82px; line-height: 1; letter-spacing: 2px;
    background: linear-gradient(180deg, #f03a3a 0%, #b51414 55%, #6e0c0c 100%);
    -webkit-background-clip: text; background-clip: text; color: transparent;
  }
  .subhead {
    position: absolute; top: 148px; left: 0; width: 100%;
    text-align: center; font-family: "Archivo Black", Arial, sans-serif;
    font-size: 24px; color: var(--deep-red);
  }
  .intro {
    position: absolute; top: 186px; left: 0; width: 100%;
    text-align: center; font-size: 22px; font-weight: 500; line-height: 29px;
    letter-spacing: 0.5px;
  }
  .regions {
    position: absolute; top: 272px; left: 0; width: 100%;
    font-size: 21px; font-weight: 500; line-height: 29px; letter-spacing: 0.6px;
  }
  .regions span { display: block; white-space: nowrap; }
  .regions .r1 { padding-left: 32px; }
  .regions .r2 { padding-left: 80px; }
  .regions .r3 { padding-left: 203px; }
  .property-photo {
    position: absolute; left: 38px; top: 380px; width: 508px; height: 337px;
    background: linear-gradient(180deg, #9fb7c9 0%, #cdb98e 35%, #7d8f52 60%, #5f7a3a 100%);
  }
  .portrait {
    position: absolute; left: 878px; top: 380px; width: 284px; height: 340px;
    border-radius: 50%;
    background: radial-gradient(ellipse at 50% 35%, #c9b8a4 0%, #a89a8a 55%, #2a2a33 100%);
  }
  .portrait-name {
    position: absolute; left: 926px; top: 718px;
    font-size: 21px; font-weight: 500; color: var(--soft-red); letter-spacing: 0.5px;
  }
  .cta {
    position: absolute; top: 754px; left: 0; width: 100%;
    text-align: center; font-family: "Montserrat", Arial, sans-serif;
    font-weight: 700; font-size: 25px; line-height: 32px; letter-spacing: 1px;
    color: var(--bright-red);
  }
  .contact {
    position: absolute; top: 816px; left: 0; width: 100%;
    text-align: center; font-size: 19px; font-weight: 500; line-height: 28px;
    color: var(--soft-red); letter-spacing: 0.3px;
  }
</style>
</head>
<body>
<main class="advert">
  <h2 class="kicker">RECEIVE - TAX FREE FROM THE GOVERNMENT</h2>
  <div class="rule"></div>
  <h1 class="headline">Over $100,000</h1>
  <p class="subhead">NRAS &amp; SMSFs</p>
  <p class="intro">Choose from the best range of HIGH CASHFLOW<br>properties in Queensland from $275,000 in:</p>
  <p class="regions">
    <span class="r1">* BRISBANE IPSWICH * GLADSTONE/ROCKHAMPTON * MORETON BAY REGION *</span>
    <span class="r2">* GOLD &amp; SUNSHINE COASTS * LOGAN &amp; SCENIC RIM * TOWNSVILLE &amp; MINING *</span>
    <span class="r3">* MACKAY &amp; BOWEN BASIN * TOOWOOMBA &amp; SURAT BASIN *</span>
  </p>
  <div class="property-photo" role="img" aria-label="Suburban brick house with lawn and letterbox, overlaid with Australian banknotes"></div>
  <div class="portrait" role="img" aria-label="Portrait of Warren Deakes, CEO"></div>
  <p class="portrait-name">Warren Deakes</p>
  <p class="cta">REQUEST YOUR FREE INVESTMENT KIT AND<br>INDICATIVE CASHFLOW NOW!</p>
  <p class="contact">Contact: Warren Deakes Phone: 0412 555 804 CEO &amp; Licensee Offices: Brisbane &amp; Ipswich<br>email: deakes@ridgemail.net.au www.YieldHomesQLD.net.au</p>
</main>
</body>
</html>
```